Beauty Therapy Web Design

I need a web page design for a small beauty therapy clinic, the owner is currently the only beauty therapist working there.
We require the following pages:
Home
About
Treatments
Nails
Courses
Contact
I will attach the clinics business card, treatment menu and signage so that you get a feeling for the branding colours etc.
This is the first website for the beauty therapist, she would like to attract new clients and also tourists that come in on the cruise ships. The thing that sets her apart from other clinics is that she welcomes texting for appointments.
I have selected refundable because I have never done this before so I don't know what to expect, I have the full intention of going through with it as long as I get a good design.
Feel free to ask for further information
Reason: Project extended as I am away for work and am unable to meet with the owner.
Target Market(s)
Females 18 to 50
Industry/Entity Type
Business
Look and feel
Each slider illustrates characteristics of the customer's brand and the style your logo design should communicate.

```html
<!DOCTYPE html>
<html lang="en">
<head>
<meta charset="utf-8">
<title>Lavinia Beauty Therapy</title>
<link href="https://fonts.googleapis.com/css2?family=Cinzel:wght@400;700&display=swap" rel="stylesheet">
<style>
  :root{
    --plum-deep:#6a1c6e;
    --plum:#8a2f88;
    --plum-light:#a24aa0;
    --stripe:rgba(205,140,205,0.22);
    --gold:#f6ef22;
    --white:#ffffff;
    --orange:#f08a0c;
    --orange-light:#fbb42e;
    --rule:#e15fb4;
    --gap:#f6eef4;
  }
  *{margin:0;padding:0;box-sizing:border-box}
  html,body{width:1200px;height:900px;overflow:hidden;background:var(--gap)}
  .stage{position:relative;width:1200px;height:900px;overflow:hidden;font-family:'Cinzel',serif}
  .hero{
    position:absolute;left:0;top:0;width:1200px;height:695px;
    background:
      radial-gradient(ellipse at 45% 15%, var(--plum-light) 0%, var(--plum) 45%, var(--plum-deep) 100%);
  }
  .floral-art{
    position:absolute;left:720px;top:60px;width:380px;height:560px;
    background:radial-gradient(ellipse at 55% 45%, rgba(230,170,230,0.35) 0%, rgba(200,130,200,0.15) 50%, rgba(0,0,0,0) 75%);
  }
  .stripe{position:absolute;top:0;height:695px;background:var(--stripe)}
  .stripe.s1{left:1040px;width:55px}
  .stripe.s2{left:1110px;width:14px}
  .stripe.s3{left:1140px;width:40px}
  .brand{
    position:absolute;left:0;top:232px;width:1176px;text-align:center;
    font-family:'Cinzel',serif;font-weight:700;font-size:66px;color:var(--gold);
    letter-spacing:1px;line-height:80px;
  }
  .tagline{
    position:absolute;left:0;top:338px;width:1176px;text-align:center;
    font-family:'Cinzel',serif;font-weight:400;font-size:29px;color:var(--white);
    letter-spacing:2px;text-shadow:0 2px 3px rgba(0,0,0,0.55);
  }
  .enter-button{position:absolute;left:971px;top:514px;width:90px;height:90px}
  .enter-label{
    position:absolute;right:42px;top:614px;
    font-family:'Cinzel',serif;font-size:30px;color:var(--white);letter-spacing:2px;
    text-shadow:0 2px 3px rgba(0,0,0,0.5);
  }
  .rule{position:absolute;left:0;top:695px;width:1200px;height:4px;background:var(--rule)}
  .gallery{position:absolute;left:0;top:699px;width:1200px;height:201px}
  .tile{position:absolute;top:0;height:201px}
  .tile.face{left:0;width:212px;background:linear-gradient(135deg,#e2b68e,#b77a52 60%,#7a4b30)}
  .tile.candle{left:216px;width:235px;background:linear-gradient(160deg,#f3e2e6,#e7b9c4 55%,#d48fa2)}
  .tile.footbath{left:455px;width:269px;background:linear-gradient(180deg,#eec7b8,#d79a86 55%,#c98b74)}
  .tile.hands{left:728px;width:270px;background:linear-gradient(160deg,#f4efec,#e7cfc0 50%,#8c3a2c)}
  .tile.cleanse{left:1002px;width:198px;background:linear-gradient(135deg,#f7ebe4,#f0d3c3 55%,#e0b49c)}
</style>
</head>
<body>
<main class="stage">
  <section class="hero">
    <div class="floral-art" role="img" aria-label="Soft floral flourish decoration"></div>
    <div class="stripe s1"></div>
    <div class="stripe s2"></div>
    <div class="stripe s3"></div>

    <h1 class="brand">Lavinia Beauty Therapy</h1>
    <p class="tagline">We Welcomes Texting For Appointments</p>

    <svg class="enter-button" viewBox="0 0 90 90" aria-hidden="true">
      <defs>
        <radialGradient id="btnFill" cx="45%" cy="35%" r="65%">
          <stop offset="0" stop-color="#fbb42e"/>
          <stop offset="1" stop-color="#e57a06"/>
        </radialGradient>
      </defs>
      <circle cx="45" cy="45" r="43" fill="#ffffff"/>
      <circle cx="45" cy="45" r="40" fill="url(#btnFill)"/>
      <path d="M34 25 L54 45 L34 65 L27 58 L40 45 L27 32 Z" fill="#ffffff"/>
    </svg>
    <p class="enter-label">Enter Site Now</p>
  </section>

  <div class="rule"></div>

  <section class="gallery">
    <div class="tile face" role="img" aria-label="Photo of a relaxed client receiving a facial"></div>
    <div class="tile candle" role="img" aria-label="Photo of a lit candle with a white orchid on pink towels"></div>
    <div class="tile footbath" role="img" aria-label="Photo of feet in a bowl of water with flower petals"></div>
    <div class="tile hands" role="img" aria-label="Photo of a hand treatment over a bowl of petals"></div>
    <div class="tile cleanse" role="img" aria-label="Photo of foam cleanser applied to skin"></div>
  </section>
</main>
</body>
</html>
```